PPE EQIUPMENT

WE WOULD LIKE TO PRODUCE 2 DIFFERENT BANNERS TO BE PLACED OUTSIDE OF OUR WAREHOUSE TO ADVERTISE THAT WE HAVE FACE MASKS, HAND SANITISERS, DISINFECTANT SPRAY, FACE SHIELDS AND HAND SOAP. THE SIZE OF EACH BANNER WILL BE , portrait to be (W) 140 cm x (H) 250 cm, with 4 x eyelets. THE BANNER IS TO STATE PPE EQUIPMENT AVAILABLE HERE AND SHOW OUR PHONE NUMBER 0207-946-0381. FINALLY WE WILL REQUIRE SOME IMAGES OF THE PRODUCTS IF YOU CAN SUPPLY THESE. THANKS

```html
<!DOCTYPE html>
<html lang="en">
<head>
<meta charset="UTF-8">
<title>PPE Equipment Banner</title>
<link rel="stylesheet" href="https://fonts.googleapis.com/css2?family=Oswald:wght@700&family=Bebas+Neue&family=Arimo&family=Barlow:wght@300;500&display=swap">
<style>
  :root {
    --navy: #203a70;
    --navy-dark: #14284f;
    --white: #ffffff;
    --backdrop: #d6d6d6;
    --eyelet-grey: #858585;
  }
  * { margin: 0; padding: 0; box-sizing: border-box; }
  html, body {
    width: 960px;
    height: 1200px;
    overflow: hidden;
    background: var(--backdrop);
  }
  .banner {
    position: absolute;
    left: 156px;
    top: 20px;
    width: 648px;
    height: 1160px;
    background: var(--white);
    overflow: hidden;
  }
  .eyelet {
    position: absolute;
    width: 34px;
    height: 34px;
    border-radius: 50%;
    border: 4px solid var(--eyelet-grey);
    background: transparent;
  }
  .eyelet--top-left { left: 13px; top: 11px; }
  .eyelet--top-right { right: 13px; top: 11px; }
  .eyelet--bottom-left { left: 13px; bottom: 11px; border-color: var(--navy-dark); z-index: 2; }
  .eyelet--bottom-right { right: 13px; bottom: 11px; border-color: var(--navy-dark); z-index: 2; }

  .headline {
    position: absolute;
    left: 0; right: 0;
    top: 56px;
    text-align: center;
    font-family: 'Oswald', sans-serif;
    font-weight: 700;
    font-size: 90px;
    line-height: 1;
    letter-spacing: -2px;
    color: var(--navy);
    white-space: nowrap;
  }
  .subline {
    position: absolute;
    left: 0; right: 0;
    top: 164px;
    text-align: center;
    font-family: 'Arimo', sans-serif;
    font-size: 50px;
    line-height: 1;
    color: var(--navy);
    white-space: nowrap;
  }
  .phone-band {
    position: absolute;
    left: 0; right: 0;
    top: 226px;
    height: 112px;
    background: var(--navy);
    display: flex;
    align-items: center;
    justify-content: center;
  }
  .phone-number {
    font-family: 'Oswald', sans-serif;
    font-weight: 700;
    font-size: 80px;
    line-height: 1;
    letter-spacing: -1px;
    color: var(--white);
    white-space: nowrap;
  }
  .product-list {
    position: absolute;
    left: 40px;
    top: 365px;
    list-style: none;
  }
  .product {
    display: flex;
    align-items: center;
    height: 108px;
    margin-bottom: 14px;
  }
  .product-icon {
    width: 142px;
    height: 108px;
    border-radius: 8px;
    background: linear-gradient(160deg, #2a4a86, var(--navy));
    flex: none;
  }
  .product-name {
    margin-left: 17px;
    margin-top: -14px;
    font-family: 'Bebas Neue', sans-serif;
    font-size: 64px;
    line-height: 1;
    color: var(--navy);
    white-space: nowrap;
  }
  .footer-band {
    position: absolute;
    left: 0; right: 0;
    bottom: 0;
    height: 171px;
    background: var(--navy);
    color: var(--white);
    text-align: center;
  }
  .company-name {
    position: absolute;
    left: 0; right: 0;
    top: 30px;
    font-family: 'Barlow', sans-serif;
    font-weight: 500;
    font-size: 50px;
    line-height: 1;
    letter-spacing: 1.5px;
    white-space: nowrap;
  }
  .company-tagline {
    position: absolute;
    left: 0; right: 0;
    top: 92px;
    font-family: 'Barlow', sans-serif;
    font-weight: 300;
    font-size: 31px;
    line-height: 1;
    letter-spacing: 1.5px;
    white-space: nowrap;
  }
</style>
</head>
<body>
  <main class="banner">
    <span class="eyelet eyelet--top-left"></span>
    <span class="eyelet eyelet--top-right"></span>

    <h1 class="headline">PPE EQUIPMENT</h1>
    <p class="subline">AVAILABLE HERE</p>

    <div class="phone-band">
      <span class="phone-number">0207-946-0381</span>
    </div>

    <ul class="product-list">
      <li class="product">
        <div class="product-icon" role="img" aria-label="Face mask icon"></div>
        <span class="product-name">FACE MASKS</span>
      </li>
      <li class="product">
        <div class="product-icon" role="img" aria-label="Hands under a sanitiser pump bottle icon"></div>
        <span class="product-name">HAND SANITISERS</span>
      </li>
      <li class="product">
        <div class="product-icon" role="img" aria-label="Disinfectant spray bottle icon"></div>
        <span class="product-name">DISINFECTANT SPRAY</span>
      </li>
      <li class="product">
        <div class="product-icon" role="img" aria-label="Face shield icon"></div>
        <span class="product-name">FACE SHIELDS</span>
      </li>
      <li class="product">
        <div class="product-icon" role="img" aria-label="Hand holding a bar of soap icon"></div>
        <span class="product-name">HAND SOAP</span>
      </li>
    </ul>

    <footer class="footer-band">
      <p class="company-name">NORTHGATE INTERIORS</p>
      <p class="company-tagline">TRADE FURNITURE SOLUTIONS</p>
    </footer>

    <span class="eyelet eyelet--bottom-left"></span>
    <span class="eyelet eyelet--bottom-right"></span>
  </main>
</body>
</html>
```